Dyrano In-home Personal Training

I would like to have some eye-catching business card design. Opened to any ideas.

The business idea: mobile fitness - train clients at their places

Target Market(s)

General population, 20-60 years old

Industry/Entity Type

Fitness

Contact Information for Business Card

The information to include:
Name: Marta
Call or text: 306-555-0187
Website: Dyrano.ca
Please use the attached logo

Requirements
Should not have
• No orange or purple colours please

```html
<!DOCTYPE html>
<html lang="en">
<head>
<meta charset="utf-8">
<title>Dyrano – Business Card</title>
<link rel="stylesheet" href="https://fonts.googleapis.com/css2?family=Poppins:wght@300;400&display=swap">
<style>
  :root {
    --backdrop: #1e1e1e;
    --card: #ffffff;
    --ink: #3a3a3c;
    --ink-soft: #5a5a5c;
  }
  * { margin: 0; padding: 0; box-sizing: border-box; }
  html, body {
    width: 1200px;
    height: 900px;
    overflow: hidden;
    background: var(--backdrop);
    font-family: "Poppins", sans-serif;
    color: var(--ink);
  }
  .stage {
    width: 1200px;
    height: 900px;
    display: flex;
    flex-direction: column;
    align-items: center;
    justify-content: center;
    gap: 44px;
  }
  .card {
    width: 630px;
    height: 360px;
    background: var(--card);
    position: relative;
    overflow: hidden;
  }

  /* Front: brand lockup */
  .card-front {
    display: flex;
    align-items: center;
    justify-content: center;
  }
  .brand-lockup {
    display: flex;
    align-items: center;
    gap: 18px;
  }
  .brand-square {
    width: 44px;
    height: 44px;
    border: 2px solid var(--ink);
  }
  .brand-text { display: flex; flex-direction: column; }
  .brand-name {
    font-weight: 300;
    font-size: 52px;
    letter-spacing: 14px;
    line-height: 1;
    color: var(--ink);
  }
  .brand-tagline {
    font-weight: 300;
    font-size: 11px;
    letter-spacing: 3.2px;
    text-transform: uppercase;
    margin-top: 6px;
    color: var(--ink);
  }

  /* Back: contact side */
  .card-back .brand-mark {
    position: absolute;
    left: 34px;
    top: 40px;
    display: flex;
    align-items: center;
    gap: 16px;
  }
  .card-back .brand-mark .brand-square {
    width: 70px;
    height: 70px;
    border-width: 3px;
  }
  .card-back .brand-mark .brand-name {
    font-size: 64px;
    letter-spacing: 12px;
  }
  .contact {
    position: absolute;
    left: 330px;
    top: 196px;
  }
  .contact-name {
    font-weight: 300;
    font-size: 30px;
    letter-spacing: 1.5px;
    line-height: 1.1;
    margin-bottom: 10px;
  }
  .contact-line {
    font-weight: 300;
    font-size: 14px;
    letter-spacing: 1px;
    line-height: 1.7;
    color: var(--ink-soft);
  }
  .contact-line .sep { margin: 0 8px; }
</style>
</head>
<body>
  <main class="stage">
    <section class="card card-front">
      <div class="brand-lockup">
        <div class="brand-square"></div>
        <div class="brand-text">
          <span class="brand-name">Dyrano</span>
          <span class="brand-tagline">In-home personal training</span>
        </div>
      </div>
    </section>

    <section class="card card-back">
      <div class="brand-mark">
        <div class="brand-square"></div>
        <span class="brand-name">Dyrano</span>
      </div>
      <div class="contact">
        <p class="contact-name">Marta</p>
        <p class="contact-line">Call<span class="sep">|</span>306-555-0187</p>
        <p class="contact-line">Visit<span class="sep">|</span>www.Dyrano.ca</p>
      </div>
    </section>
  </main>
</body>
</html>
```